Birchmoor Yard Care_2015 New Cards_V1

We need an enhanced business card from what we have today. We are a Landscaping company and we have an existing Logo and text info that we would like to include.
Text to include:
In business for over 20 years,Fully Insured, Weekly Lawn Maintenance, Spring & Fall Clean-up, Todd Pierson, 203-555-0147, www.birchmooryardcarect.example, Visit our Website for additional Lawn Care Services or email directly at TODD@BIRCHMOORYARDCARE.EXAMPLE, We appreciate your business.
We want full color background and we will want to take this design and work with a printer that does high graphic silk screen cards. The colors we have thought about are Black, with our Green Logo, with Gold Text...we are open to different colors, we just want the card to wow!

Target Market(s)

Lawn Care Maintenance

Industry/Entity Type

Lawn Care

Contact Information for Business Card

Text to include:
In business for over 20 years, Fully Insured, Weekly Lawn Maintenance, Spring & Fall Clean-up, Todd Pierson, 203-555-0147, www.birchmooryardcarect.example, Visit our Website for additional Lawn Care Services or email directly at TODD@BIRCHMOORYARDCARE.EXAMPLE, We appreciate your business.

Requirements
Must have
• Logo, text details about how to reach us, standard size business cards that go horizontal.
Nice to have
• background colors, background designs, raised embossed lettering, rounded corners(2 or 4),

```html
<!DOCTYPE html>
<html lang="en">
<head>
<meta charset="utf-8">
<title>Birchmoor Yard Care – Business Cards</title>
<link rel="stylesheet" href="https://fonts.googleapis.com/css2?family=Lato:wght@400;700;900&display=swap">
<style>
  :root {
    --page: #ece9e4;
    --card-white: #ffffff;
    --brand-green: #0b4615;
    --text-light: #ffffff;
    --shadow: rgba(0, 0, 0, 0.22);
  }
  html, body {
    margin: 0;
    padding: 0;
    width: 1200px;
    height: 900px;
    overflow: hidden;
    background: var(--page);
    font-family: "Lato", sans-serif;
  }
  .canvas {
    position: relative;
    width: 1200px;
    height: 900px;
  }
  .card {
    position: absolute;
    width: 560px;
    height: 320px;
    background: var(--card-white);
    box-shadow: 0 10px 26px var(--shadow);
    overflow: hidden;
  }
  .card--back { left: 70px; top: 90px; }
  .card--front { left: 570px; top: 490px; }

  .card__top {
    height: 148px;
    display: flex;
    align-items: center;
    justify-content: center;
  }
  .card__band {
    position: absolute;
    left: 0; right: 0; bottom: 0;
    height: 172px;
    background: var(--brand-green);
    color: var(--text-light);
  }

  .brand {
    display: flex;
    align-items: center;
    gap: 10px;
    color: var(--brand-green);
    font-weight: 900;
    font-size: 27px;
    letter-spacing: 3px;
    text-transform: uppercase;
  }
  .brand__dot {
    width: 16px;
    height: 16px;
    border-radius: 50%;
    background: var(--brand-green);
  }
  .card--back .card__top { padding-top: 6px; }

  .services {
    text-align: center;
    padding-top: 22px;
  }
  .services__line {
    margin: 0 0 6px;
    font-size: 15px;
    font-weight: 700;
  }
  .services__sep {
    display: inline-block;
    width: 6px;
    height: 6px;
    border-radius: 50%;
    background: var(--text-light);
    margin: 0 8px 2px;
    vertical-align: middle;
  }
  .services__note {
    margin: 18px 0 0;
    font-size: 14px;
    line-height: 1.45;
  }

  .contact {
    display: flex;
    justify-content: space-between;
    padding: 26px 34px 0 40px;
  }
  .contact__person {
    text-align: right;
    padding-top: 8px;
  }
  .contact__name {
    margin: 0;
    font-size: 23px;
    font-weight: 400;
  }
  .contact__role {
    margin: 2px 0 12px;
    font-size: 15px;
  }
  .contact__address {
    margin: 0;
    font-size: 16px;
    line-height: 1.35;
    font-style: normal;
  }
  .contact__list {
    list-style: none;
    margin: 0;
    padding: 0;
  }
  .contact__item {
    display: flex;
    align-items: center;
    gap: 8px;
    font-size: 14px;
    margin-bottom: 6px;
  }
  .contact__icon {
    width: 16px;
    height: 16px;
    flex: none;
  }
</style>
</head>
<body>
<main class="canvas">

  <section class="card card--back" aria-label="Card back">
    <div class="card__top">
      <div class="brand"><span class="brand__dot"></span>Birchmoor Yard Care</div>
    </div>
    <div class="card__band">
      <div class="services">
        <p class="services__line">In business for over 20 years<span class="services__sep"></span>Fully Insured</p>
        <p class="services__line">Weekly Lawn Maintenance<span class="services__sep"></span>Spring &amp; Fall Clean-up</p>
        <p class="services__note">Visit our Website for additional Lawn Care Services or email<br>directly at TODD@BIRCHMOORYARDCARE.EXAMPLE</p>
      </div>
    </div>
  </section>

  <section class="card card--front" aria-label="Card front">
    <div class="card__top">
      <div class="brand"><span class="brand__dot"></span>Birchmoor Yard Care</div>
    </div>
    <div class="card__band">
      <div class="contact">
        <div class="contact__person">
          <h2 class="contact__name">Dale Moreno</h2>
          <p class="contact__role">Managing Director</p>
          <address class="contact__address">1234, Address GoesHere<br>Country, 12345</address>
        </div>
        <ul class="contact__list">
          <li class="contact__item">
            <svg class="contact__icon" viewBox="0 0 16 16" aria-hidden="true"><rect width="16" height="16" rx="2" fill="#fff"/><path d="M4 5c0 4 3 7 7 7l1-2-2-1-1 1c-1-.5-2-1.5-2.5-2.5l1-1-1-2z" fill="#0b4615"/></svg>
            123-456-7890
          </li>
          <li class="contact__item">
            <svg class="contact__icon" viewBox="0 0 16 16" aria-hidden="true"><rect width="16" height="16" rx="2" fill="#fff"/><rect x="4" y="6" width="8" height="6" fill="#0b4615"/><rect x="5" y="3" width="6" height="3" fill="none" stroke="#0b4615"/></svg>
            123-456-7890
          </li>
          <li class="contact__item">
            <svg class="contact__icon" viewBox="0 0 16 16" aria-hidden="true"><rect width="16" height="16" rx="2" fill="#fff"/><rect x="3" y="5" width="10" height="7" fill="#0b4615"/><path d="M3 5l5 4 5-4" fill="none" stroke="#fff"/></svg>
            info@birchmoor.example
          </li>
          <li class="contact__item">
            <svg class="contact__icon" viewBox="0 0 16 16" aria-hidden="true"><rect width="16" height="16" rx="2" fill="#fff"/><path d="M7 9l2-2M6 7l-2 2a1.5 1.5 0 0 0 3 3l2-2M10 9l2-2a1.5 1.5 0 0 0-3-3L7 6" fill="none" stroke="#0b4615" stroke-width="1.4"/></svg>
            www.birchmoor.example
          </li>
        </ul>
      </div>
    </div>
  </section>

</main>
</body>
</html>
```